Website Design for PawRank - New Digital Agency

We are creating a new digital marketing agency and need a new website. I have attached the logo. Our niche is going to be veterinarians. Use the same colors as in the logo (blue, white and gray).

I want real pictures of real people in this and not just boring stock photos. It needs to be related to the industry.

Home page (example:https://trellmarsh.com/)
Service page (example: https://dovequist.com/consulting/)
Case study page (example: https://www.harlowfinchley.com/seo/case-study/)

I will continue to update this brief.
Updates

I updated the brief with some additional sample sites 2 days ago and want to see more designs. I won't need that may more days ...just a few more.

Target Market(s)

veterinarians

Font styles to use
Sans Serif

Requirements
Must have
• I want a very clean looking site. Use the same colors as in the logo (blue, white and gray).
Nice to have
• We need to build this with the idea that the purpose is to generate leads for our business.
• Home page (example:https://trellmarsh.com/)
• Service page (example: https://dovequist.com/consulting/)
• Case study page (example: https://www.harlowfinchley.com/seo/case-study/)

```html
<!DOCTYPE html>
<html lang="en">
<head>
<meta charset="utf-8">
<title>PawRank – Get More Traffic to your Veterinarian Website</title>
<link rel="stylesheet" href="https://fonts.googleapis.com/css2?family=Montserrat:wght@300;400;500;600&family=Playfair+Display:ital@1&display=swap">
<style>
:root{
  --blue:#1457a8;
  --blue-dark:#0f4a94;
  --navy:#0e1b38;
  --ink:#333a44;
  --muted:#5c6470;
  --gray-logo:#b4b7bc;
  --pill:#e4e5e8;
  --orange:#f7a21b;
  --white:#ffffff;
  --v-gray:#5e5f62;
}
*{box-sizing:border-box;margin:0;padding:0}
html,body{width:1200px;height:3523px;overflow:hidden}
body{position:relative;font-family:'Montserrat',sans-serif;color:var(--ink);background:var(--white)}
.abs{position:absolute}

/* hero */
.hero{left:0;top:0;width:1200px;height:602px;background:linear-gradient(180deg,#eef0f3 0%,#f5f6f8 60%,#ffffff 100%)}
.hero-photo{left:547px;top:82px;width:653px;height:465px;background:linear-gradient(135deg,#e6e9ee 0%,#c7d3e4 45%,#8fa6c6 70%,#eef0f3 100%);border-radius:4px}
.brand{left:77px;top:42px;display:flex;align-items:center;gap:10px;font-size:30px;font-weight:600;color:var(--blue)}
.brand-dot{width:16px;height:16px;border-radius:50%;background:var(--blue)}
.nav{left:663px;top:38px;display:flex;gap:20px;font-size:13px;color:var(--muted)}
.nav-btn{left:984px;top:27px;width:146px;height:40px;border-radius:20px;background:var(--orange);color:#1c1c1c;font-size:13px;font-weight:500;display:flex;align-items:center;justify-content:center}
.hero-title{left:81px;top:146px;font-size:46px;font-weight:400;line-height:56px;color:#2e3440;letter-spacing:.5px}
.accent{color:var(--blue)}
.hero-sub{left:79px;top:326px;width:460px;font-size:15px;line-height:24px;color:var(--muted)}
.signup{width:368px;height:61px;border-radius:31px;background:var(--pill)}
.signup span{position:absolute;left:31px;top:21px;font-size:13px;color:#4a4f58}
.signup-btn{height:44px;width:147px;border-radius:22px;background:var(--blue);color:var(--white);font-size:13px;font-weight:600;display:flex;align-items:center;justify-content:center;box-shadow:0 10px 22px rgba(20,87,168,.35)}

/* press */
.press{top:640px;left:0;width:1200px;height:48px}
.press-name{top:0;width:180px;margin-left:-90px;text-align:center;font-size:32px;font-weight:600;color:var(--gray-logo)}

/* testimonial band */
.band{left:0;top:770px;width:1200px;height:417px;background:var(--blue)}
.quote-mark{color:rgba(255,255,255,.18)}
.band-quote{left:270px;top:858px;width:660px;text-align:center;color:var(--white);font-size:27px;line-height:38px;font-weight:400}
.band-name{left:0;top:1030px;width:1200px;text-align:center;color:var(--white);font-size:14px;font-weight:500}
.avatar{border-radius:50%;background:radial-gradient(circle at 50% 40%,#9aa0a8,#4a4e55);border:3px solid var(--white)}

/* story */
.story-title{left:124px;top:1358px;font-size:41px;line-height:52px;font-weight:400;color:#2e3440}
.story-body{left:124px;top:1527px;width:536px;font-size:14.5px;line-height:29px;color:#3b414b;font-weight:500}
.story-body p{margin-bottom:29px}
.cta{left:111px;top:2194px;width:351px;height:51px;border-radius:26px;background:var(--blue);color:var(--white);font-size:16px;font-weight:600;display:flex;align-items:center;justify-content:center;box-shadow:0 14px 28px rgba(20,87,168,.35)}
.card{left:748px;top:1352px;width:327px;height:451px;background:var(--white);box-shadow:0 6px 30px rgba(0,0,0,.08);padding:46px 36px}
.card-quote{font-family:'Playfair Display',serif;font-style:italic;font-size:26px;line-height:36px;color:#6b717a}
.card-name{margin-top:22px;font-size:14px;line-height:21px;color:#7d838c}
.workspace{left:643px;top:2127px;width:557px;height:418px;background:radial-gradient(ellipse at 55% 45%,#f2c6d8 0%,#c9d8ef 35%,#eef0f3 70%,#ffffff 100%)}

/* lead section */
.lead{left:0;top:2633px;width:1200px;height:890px;background:var(--navy)}
.lead-photo{left:0;top:2633px;width:650px;height:780px;background:linear-gradient(135deg,#d9dde3 0%,#9fb2cc 50%,#4f6f9e 100%);clip-path:polygon(0 0,643px 0,205px 767px,0 349px)}
.v-shape{left:0;top:2600px}
.lead-title{left:661px;top:2737px;font-size:41px;line-height:53px;color:var(--white);font-weight:400}
.lead-sub{left:666px;top:2924px;width:440px;font-size:15px;line-height:24px;color:#c9cfd9}
.footer-col{top:3236px;font-size:12.5px;color:var(--white)}
.footer-col h4{font-size:14px;font-weight:600;margin-bottom:18px}
.footer-col li{list-style:none;line-height:25px;font-weight:400}
.social{top:3460px;width:14px;height:14px;border-radius:50%;background:var(--white)}
</style>
</head>
<body>

<section class="hero abs"></section>
<div class="hero-photo abs" role="img" aria-label="Veterinarian in blue scrubs examining a dog on a clinic table"></div>

<div class="brand abs">PawRank<span class="brand-dot"></span></div>
<nav class="nav abs"><span>Home</span><span>About</span><span>Tools</span><span>Newsletter</span><span>Contact</span></nav>
<div class="nav-btn abs">Sign up/Login</div>

<h1 class="hero-title abs">Get <span class="accent">More Traffic</span><br>to your Veterinarian<br>Website</h1>
<p class="hero-sub abs">Enter your email below to get access to my proven SEO and traffic tips</p>
<div class="signup abs" style="left:70px;top:401px"><span>Email Address</span></div>
<div class="signup-btn abs" style="left:361px;top:410px">Sign Up Now!</div>

<div class="press abs">
  <span class="press-name abs" style="left:233px">Larkfield</span>
  <span class="press-name abs" style="left:421px">Brightpost</span>
  <span class="press-name abs" style="left:602px">Vexora</span>
  <span class="press-name abs" style="left:784px">Shopmere</span>
  <span class="press-name abs" style="left:967px">Larkfield</span>
</div>

<section class="band abs"></section>
<svg class="quote-mark abs" style="left:112px;top:862px" width="106" height="90" viewBox="0 0 106 90" aria-hidden="true">
  <path fill="currentColor" d="M0 22Q0 0 22 0H46V44H26V66H46V90H22Q0 90 0 68ZM58 22Q58 0 80 0H106V44H84V66H106V90H80Q58 90 58 68Z"/>
</svg>
<svg class="quote-mark abs" style="left:982px;top:999px" width="106" height="90" viewBox="0 0 106 90" aria-hidden="true">
  <path fill="currentColor" d="M106 68Q106 90 84 90H60V46H80V24H60V0H84Q106 0 106 22ZM48 68Q48 90 26 90H0V46H22V24H0V0H26Q48 0 48 22Z"/>
</svg>
<p class="band-quote abs">Lorem ipsum dolor sit amet, ea pro brute facer propriae, nec epicurei senserit pericula cu. Ea graece animal equidem cum. Ei graece omittantur vel scaevola qui te.</p>
<p class="band-name abs">Marcus Delaney - Author &amp; Marketer</p>

<div class="avatar abs" style="left:264px;top:1139px;width:96px;height:96px" role="img" aria-label="Client portrait"></div>
<div class="avatar abs" style="left:401px;top:1139px;width:96px;height:96px" role="img" aria-label="Client portrait"></div>
<div class="avatar abs" style="left:527px;top:1115px;width:144px;height:144px;background:radial-gradient(circle at 50% 40%,#3f6fb0,#0f2a55)" role="img" aria-label="Featured client portrait"></div>
<div class="avatar abs" style="left:702px;top:1139px;width:96px;height:96px" role="img" aria-label="Client portrait"></div>
<div class="avatar abs" style="left:839px;top:1139px;width:96px;height:96px" role="img" aria-label="Client portrait"></div>

<h2 class="story-title abs">See How I Got <span class="accent">More Web<br>Traffic</span> to my Veterinary<br>Website</h2>
<div class="story-body abs">
  <p>Lorem ipsum dolor sit amet, ea pro brute facer propriae, nec epicurei senserit pericula cu. Ea graece animal equidem cum. Ei graece omittantur vel. Habeo persius scaevola qui te. Duo eu mucius nostrum. Causae docendi temporibus vel at. Usu ad postea fabellas, qui nostro iracundia ei. Te vis dicat ludus, an per tale detraxit. Quis vulputate ea pri, essent noluisse sea ex, te nam enim falli. Inciderint temporibus ne cum</p>
  <p>Prima cetero intellegebat id eum, ius iriure impetus no, enim nominati suscipiantur cu pro. Eum an aliquid adipisci praesent, id pro laoreet feugait incorrupte. Ex sed probo nihil quidam. Meliore docendi mandamus ius no. Quo eirmod nostrum intellegebat ad, id duo accusamus</p>
  <p>Id quo munere delenit accusamus, his id probatus eleifend, ei fugit simul sed. Cu maiorum suscipiantur sit. Te vis dicat ludus, an per tale detraxit. Quis vulputate ea pri, essent noluisse sea ex, te nam enim falli. Inciderint temporibus ne cum.</p>
  <p>Lorem ipsum dolor sit amet, ea pro brute facer propriae, nec epicurei senserit pericula cu. Ea graece animal equidem cum. Ei graece omittantur vel. Habeo persius scaevola qui te. Duo eu mucius nostrum. Causae docendi temporibus vel at. Usu ad postea fabellas, qui nostro iracundia ei. Quo eirmod nostrum intellegebat ad, id duo accusamus.</p>
</div>
<div class="cta abs">Read More about Getting Results</div>

<aside class="card abs">
  <p class="card-quote">Lorem ipsum dolor sit amet, ea pro brute elit facer lorem propriae, nec epicurei senserit pericula cu. Ea graece animal equidem cum. Ei graece omittantur vel scaevola qui te.</p>
  <p class="card-name">Marcus Delaney<br>Author &amp; Marketer</p>
</aside>
<div class="workspace abs" role="img" aria-label="Desk with a computer monitor sprouting colourful lines of marketing icons, a lamp and a kettle"></div>

<section class="lead abs"></section>
<div class="lead-photo abs" role="img" aria-label="Smiling veterinarian with a stethoscope holding a dog"></div>
<svg class="v-shape abs" width="680" height="820" viewBox="0 0 680 820" aria-hidden="true">
  <path fill="var(--v-gray)" d="M643 10L662 26L212 810L190 810L0 420L0 360L205 760Z"/>
</svg>

<h2 class="lead-title abs">Do You Want More<br>Traffic to your<br>Veterinary Website?</h2>
<p class="lead-sub abs">Enter your email below to get access to my proven SEO and traffic tips</p>
<div class="signup abs" style="left:648px;top:2999px;width:371px"><span>Email Address</span></div>
<div class="signup-btn abs" style="left:938px;top:3007px;width:148px">Sign Up Now!</div>

<div class="footer-col abs" style="left:633px"><h4>What We Do</h4><ul><li>Solutions</li><li>Products</li><li>Resources</li><li>Our Customers</li></ul></div>
<div class="footer-col abs" style="left:776px"><h4>Company</h4><ul><li>About Us</li><li>Our Team</li><li>Careers</li><li>Legal</li><li>Contact</li></ul></div>
<div class="footer-col abs" style="left:896px"><h4>Support</h4><ul><li>Features</li><li>Pricing</li><li>Team</li><li>Contact</li><li>Login</li></ul></div>
<div class="footer-col abs" style="left:1000px"><h4>Legal</h4><ul><li>Legal</li><li>Terms Of Service</li><li>Privacy Policy</li></ul></div>

<span class="social abs" style="left:1023px" role="img" aria-label="Social link"></span>
<span class="social abs" style="left:1053px" role="img" aria-label="Social link"></span>
<span class="social abs" style="left:1083px" role="img" aria-label="Social link"></span>

</body>
</html>
```